Home care agency

Current website QTRBLOOMS.com. Need to update and reformat to different pages. use my info from my current website

Target Market(s)

adult children

Industry/Entity Type

Home Health

Coding

Coded - Design and coding required

Number of Pages Required

4 page

Font styles to use
Sans Serif

Colors
3276b5
33a6d7
3277b5
85cae6
85acd3

```html
<!DOCTYPE html>
<html lang="en">
<head>
<meta charset="utf-8">
<title>QTR Blooms Health &amp; Home Services</title>
<link rel="stylesheet" href="https://fonts.googleapis.com/css2?family=Raleway:wght@400;500;600;700&family=Open+Sans:wght@400;600;700&display=swap">
<style>
:root{
  --blue-deep:#3276b5;
  --blue-mid:#3277b5;
  --blue-sky:#33a6d7;
  --blue-light:#85cae6;
  --blue-soft:#85acd3;
  --navy:#1d4a9a;
  --ink:#2b2b2b;
  --text:#555;
  --field:#f0f0f0;
  --white:#fff;
}
*{box-sizing:border-box;margin:0;padding:0}
html,body{width:1200px;height:4237px;overflow:hidden;background:var(--white)}
body{position:relative;font-family:"Open Sans",Arial,sans-serif;color:var(--text)}
.abs{position:absolute}

/* header */
.site-header{position:absolute;left:0;top:0;width:1200px;height:171px}
.contact-chip{position:absolute;display:flex;align-items:center;gap:10px;font-family:"Raleway",Arial,sans-serif;font-size:17px;color:var(--ink);font-weight:500}
.nav-link{position:absolute;top:82px;font-family:"Raleway",Arial,sans-serif;font-size:19px;color:var(--blue-deep)}
.nav-link.active{color:var(--ink)}
.brand-mark{position:absolute;left:523px;top:24px;width:132px;height:132px;border-radius:50%;border:3px solid var(--blue-light);display:flex;align-items:center;justify-content:center;text-align:center;font-family:"Raleway",Arial,sans-serif;font-size:18px;font-weight:500;color:var(--blue-soft);line-height:1.2}

/* hero */
.hero{position:absolute;left:0;top:171px;width:1200px;height:562px;background:linear-gradient(100deg,#7b6a5c 0%,#b5a796 30%,#d8d2c8 55%,#8c8078 80%,#5d524c 100%)}
.hero-title{position:absolute;left:0;width:690px;text-align:center;font-family:"Raleway",Arial,sans-serif;font-weight:700;color:var(--white)}
.hero-brand{top:190px;font-size:76px;color:var(--navy)}
.hero-line{font-size:42px}
.hero-dots{position:absolute;left:578px;top:530px;display:flex;gap:8px}
.hero-dots span{width:12px;height:12px;border-radius:50%;background:var(--white)}
.hero-dots span:first-child{background:var(--blue-sky)}

/* welcome */
.welcome-photo{position:absolute;left:107px;top:814px;width:411px;height:493px;background:linear-gradient(180deg,#e9e6e2,#d7d2cc)}
.welcome-title{position:absolute;left:551px;top:852px;font-family:"Raleway",Arial,sans-serif;font-size:44px;font-weight:600;color:var(--ink)}
.welcome-title span{color:var(--blue-sky)}
.welcome-text{position:absolute;left:554px;top:922px;font-size:17px;line-height:34.3px;color:var(--text);white-space:nowrap}
.btn-read{position:absolute;left:549px;top:1159px;width:158px;height:46px;border-radius:23px;background:var(--navy);color:var(--white);display:flex;align-items:center;justify-content:center;gap:12px;font-family:"Raleway",Arial,sans-serif;font-weight:700;font-size:17px}

/* why */
.why{position:absolute;left:0;top:1307px;width:1200px;height:626px;background:linear-gradient(180deg,#3ba8d9,#4aaedb 60%,#3aa3d4)}
.section-title-light{position:absolute;left:0;width:1200px;text-align:center;top:60px;font-family:"Raleway",Arial,sans-serif;font-weight:700;font-size:34px;color:var(--white)}
.why-tile{position:absolute;width:314px;border-radius:4px;display:flex;align-items:center;justify-content:center;text-align:center;padding:0 14px;font-family:"Raleway",Arial,sans-serif;font-weight:700;font-size:19px;line-height:28px;color:var(--white);text-shadow:0 1px 3px rgba(0,0,0,.35)}

/* schedule */
.schedule-title{position:absolute;left:0;width:1200px;top:2013px;text-align:center;font-family:"Raleway",Arial,sans-serif;font-weight:600;font-size:44px;color:var(--ink)}
.schedule-ring{position:absolute;top:2142px;width:220px;height:220px;border-radius:50%;border:4px solid var(--blue-sky)}
.schedule-text{position:absolute;top:2383px;width:300px;text-align:center;font-size:17px;line-height:34.5px;color:var(--text)}

/* services */
.services{position:absolute;left:0;top:2532px;width:1200px;height:375px;overflow:hidden}
.services-title{position:absolute;top:65px;font-family:"Raleway",Arial,sans-serif;font-weight:700;font-size:31px;color:var(--white)}
.service-list{position:absolute;top:108px;list-style:none}
.service-list li{display:flex;align-items:center;gap:8px;height:33.4px;font-size:15.5px;color:var(--white)}
.services-badge{position:absolute;left:543px;top:126px;width:124px;height:124px;border-radius:50%;background:var(--white);border:3px solid var(--blue-light);display:flex;align-items:center;justify-content:center;text-align:center;font-family:"Raleway",Arial,sans-serif;font-weight:500;font-size:16px;color:var(--blue-soft);line-height:1.2}

/* inquiry */
.area-map{position:absolute;left:115px;top:3066px;width:362px;height:444px;background:linear-gradient(135deg,#2d6fb5 0%,#3276b5 45%,#f2f2f2 46%,#e6e6e6 100%)}
.form-title{position:absolute;left:531px;top:2963px;font-family:"Raleway",Arial,sans-serif;font-weight:700;font-size:20px;color:var(--ink)}
.form-label{position:absolute;left:534px;font-size:11.5px;color:var(--ink)}
.form-label.strong{font-weight:700;font-size:12px}
.field{position:absolute;height:28px;background:var(--field);font-size:10px;color:#555;padding-left:11px;display:flex;align-items:center}
.radio{position:absolute;display:flex;align-items:center;gap:8px;font-size:10px;color:#444}
.radio i{width:11px;height:11px;border:1px solid #999;border-radius:50%}
.btn-submit{position:absolute;left:531px;top:3732px;width:319px;height:53px;border-radius:27px;background:var(--blue-deep);color:var(--white);display:flex;align-items:center;justify-content:center;font-family:"Raleway",Arial,sans-serif;font-weight:700;font-size:17px}

/* footer */
.site-footer{position:absolute;left:0;top:3847px;width:1200px;height:390px;background:linear-gradient(180deg,#3aa6d8,#37a2d5)}
.footer-note{position:absolute;left:120px;top:128px;width:320px;font-family:"Raleway",Arial,sans-serif;font-size:16px;line-height:26.3px;color:var(--white)}
.footer-brand{position:absolute;left:490px;top:89px;width:224px;height:224px;border-radius:50%;border:4px solid var(--white);display:flex;align-items:center;justify-content:center;text-align:center;font-family:"Raleway",Arial,sans-serif;font-size:26px;font-weight:500;color:var(--white);line-height:1.25}
.footer-contact{position:absolute;left:780px;display:flex;gap:18px;font-family:"Raleway",Arial,sans-serif;font-size:17px;line-height:26px;color:var(--white)}
.footer-contact svg{flex:none;margin-top:4px}
.copyright{position:absolute;left:113px;top:345px;font-size:12px;color:var(--white)}
</style>
</head>
<body>

<header class="site-header">
  <div class="contact-chip" style="left:110px;top:22px">
    <svg width="36" height="36" viewBox="0 0 36 36"><circle cx="18" cy="18" r="18" fill="#1d4a9a"/><rect x="10" y="12" width="16" height="12" rx="1" fill="none" stroke="#fff" stroke-width="1.8"/><path d="M10 13l8 6 8-6" fill="none" stroke="#fff" stroke-width="1.8"/></svg>
    info@qtrblooms.com
  </div>
  <div class="contact-chip" style="left:916px;top:22px">
    <svg width="36" height="36" viewBox="0 0 36 36"><circle cx="18" cy="18" r="18" fill="#1d4a9a"/><path d="M13 10c1 0 3 3 3 4s-2 2-1 3 2 3 3 3 2-1 3-1 4 2 4 3-2 3-3 3c-5 0-12-7-12-12 0-1 2-3 3-3z" fill="#fff"/></svg>
    555-014-2290
  </div>
  <span class="nav-link active" style="left:124px">Home</span>
  <span class="nav-link" style="left:211px">About</span>
  <span class="nav-link" style="left:298px">Home Care Services</span>
  <div class="brand-mark">QTR<br>Blooms</div>
  <span class="nav-link" style="left:690px;top:86px">Why Us</span>
  <span class="nav-link" style="left:792px;top:86px">Blog</span>
  <span class="nav-link" style="left:866px;top:86px">Careers</span>
  <span class="nav-link" style="left:967px;top:86px">Contact Us</span>
</header>

<section class="hero" role="img" aria-label="Photo of a nurse in a white coat caring for an elderly man at home">
  <div class="hero-title hero-brand">QTR</div>
  <div class="hero-title hero-line" style="top:276px">QTR Blooms</div>
  <div class="hero-title hero-line" style="top:333px">Health &amp; Home Services</div>
  <div class="hero-dots"><span></span><span></span><span></span></div>
</section>

<section>
  <div class="welcome-photo" role="img" aria-label="Portrait of the agency's founder, a registered nurse in a white coat"></div>
  <h1 class="welcome-title">Welcome To <span>Qtrblooms</span></h1>
  <p class="welcome-text">QTR Blooms Health Services is owned and operated by<br>Dana Whitcomb. Dana is a registered nurse and has been<br>in the health care system since 2001. She has specialized in<br>home care, cardiology, trauma and critical care. She invests in<br>future caregivers and has taught for the nursing programs at<br>Eastshore University, Bayview IHP, and Harbor College.</p>
  <div class="btn-read">Read More
    <svg width="16" height="14" viewBox="0 0 16 14"><path d="M1 7h13M9 2l5 5-5 5" fill="none" stroke="#fff" stroke-width="2"/></svg>
  </div>
</section>

<section class="why">
  <h2 class="section-title-light">WHY CHOOSE HOME CARE?</h2>
  <div class="why-tile" style="left:112px;top:161px;height:192px;background:linear-gradient(135deg,#b79b82,#8b7565)" role="img" aria-label="Caregiver talking with an elderly woman">Cost-effective</div>
  <div class="why-tile" style="left:442px;top:161px;height:192px;background:linear-gradient(135deg,#c8c2b8,#8a8279)" role="img" aria-label="Nurse walking with an elderly man in his hallway">care in the comfort of<br>their own home</div>
  <div class="why-tile" style="left:773px;top:161px;height:192px;background:linear-gradient(135deg,#a59a8e,#6f665e)" role="img" aria-label="Elderly woman relaxing at home">peace of mind to a<br>client's family</div>
  <div class="why-tile" style="left:112px;top:367px;height:194px;background:linear-gradient(135deg,#8c7666,#5e5048)" role="img" aria-label="Caregiver helping an elderly woman from a car">near or far</div>
  <div class="why-tile" style="left:442px;top:367px;height:194px;background:linear-gradient(135deg,#9c8b79,#6a5d51)" role="img" aria-label="Caregiver sharing a meal with an elderly woman">without taking away a client's<br>independence or privacy</div>
  <div class="why-tile" style="left:773px;top:367px;height:194px;background:linear-gradient(135deg,#a08d7c,#6c5c50)" role="img" aria-label="Nurse helping an elderly man on the stairs">Home Care as Easy<br>as 1-2-3!</div>
</section>

<section>
  <h2 class="schedule-title">Care Schedule/Frequency</h2>
  <div class="schedule-ring" style="left:186px;background:linear-gradient(135deg,#ece8e3,#c9bfb4)" role="img" aria-label="Smiling elderly woman in a chair"></div>
  <div class="schedule-ring" style="left:479px;background:linear-gradient(135deg,#f4f6f8,#c9d3dc)" role="img" aria-label="Doctor holding a stethoscope"></div>
  <div class="schedule-ring" style="left:761px;background:linear-gradient(135deg,#5fa7db,#1f66b8)" role="img" aria-label="Hand touching a 24-hour service symbol"></div>
  <p class="schedule-text" style="left:146px">QTR Blooms<br>non-medical visits require a<br>four hourminimum visit.</p>
  <p class="schedule-text" style="left:439px">There are no weekly<br>minimum for medical or<br>non-medical visits.</p>
  <p class="schedule-text" style="left:737px">Clients needing 24-hour care<br>can save up 30% off of services<br>by using a live-in caregiver.</p>
</section>

<section class="services">
  <svg class="abs" style="left:0;top:0" width="1200" height="375" viewBox="0 0 1200 375">
    <defs>
      <linearGradient id="skilledBg" x1="0" y1="0" x2="1" y2="1"><stop offset="0" stop-color="#37a5d7"/><stop offset="1" stop-color="#2f98d0"/></linearGradient>
      <linearGradient id="nonMedBg" x1="0" y1="0" x2="1" y2="1"><stop offset="0" stop-color="#3b7fc6"/><stop offset="1" stop-color="#2a62ad"/></linearGradient>
    </defs>
    <rect width="1200" height="375" fill="url(#nonMedBg)"/>
    <polygon points="0,0 624,0 574,375 0,375" fill="url(#skilledBg)"/>
    <polygon points="624,0 636,0 586,375 574,375" fill="#fff"/>
  </svg>
  <h3 class="services-title" style="left:117px">SKILLED CARE SERVICES</h3>
  <ul class="service-list" style="left:117px">
    <li><svg width="15" height="15" viewBox="0 0 16 16"><circle cx="8" cy="8" r="7" fill="none" stroke="#fff" stroke-width="1.6"/><path d="M4.5 8.2l2.3 2.3 4.6-4.8" fill="none" stroke="#fff" stroke-width="1.6"/></svg>Free Initial Nursing Assessment</li>
    <li><svg width="15" height="15" viewBox="0 0 16 16"><circle cx="8" cy="8" r="7" fill="none" stroke="#fff" stroke-width="1.6"/><path d="M4.5 8.2l2.3 2.3 4.6-4.8" fill="none" stroke="#fff" stroke-width="1.6"/></svg>Medication Management</li>
    <li><svg width="15" height="15" viewBox="0 0 16 16"><circle cx="8" cy="8" r="7" fill="none" stroke="#fff" stroke-width="1.6"/><path d="M4.5 8.2l2.3 2.3 4.6-4.8" fill="none" stroke="#fff" stroke-width="1.6"/></svg>Wound Care</li>
    <li><svg width="15" height="15" viewBox="0 0 16 16"><circle cx="8" cy="8" r="7" fill="none" stroke="#fff" stroke-width="1.6"/><path d="M4.5 8.2l2.3 2.3 4.6-4.8" fill="none" stroke="#fff" stroke-width="1.6"/></svg>Injections</li>
    <li><svg width="15" height="15" viewBox="0 0 16 16"><circle cx="8" cy="8" r="7" fill="none" stroke="#fff" stroke-width="1.6"/><path d="M4.5 8.2l2.3 2.3 4.6-4.8" fill="none" stroke="#fff" stroke-width="1.6"/></svg>Medical Care Assistance</li>
    <li><svg width="15" height="15" viewBox="0 0 16 16"><circle cx="8" cy="8" r="7" fill="none" stroke="#fff" stroke-width="1.6"/><path d="M4.5 8.2l2.3 2.3 4.6-4.8" fill="none" stroke="#fff" stroke-width="1.6"/></svg>Transportation to Medical Appointments</li>
    <li><svg width="15" height="15" viewBox="0 0 16 16"><circle cx="8" cy="8" r="7" fill="none" stroke="#fff" stroke-width="1.6"/><path d="M4.5 8.2l2.3 2.3 4.6-4.8" fill="none" stroke="#fff" stroke-width="1.6"/></svg>Care Plan Management</li>
  </ul>
  <div class="services-badge">QTR<br>Blooms</div>
  <h3 class="services-title" style="left:732px">NON-MEDICAL SERVICES</h3>
  <ul class="service-list" style="left:732px">
    <li><svg width="15" height="15" viewBox="0 0 16 16"><circle cx="8" cy="8" r="7" fill="none" stroke="#fff" stroke-width="1.6"/><path d="M4.5 8.2l2.3 2.3 4.6-4.8" fill="none" stroke="#fff" stroke-width="1.6"/></svg>Live-In Care</li>
    <li><svg width="15" height="15" viewBox="0 0 16 16"><circle cx="8" cy="8" r="7" fill="none" stroke="#fff" stroke-width="1.6"/><path d="M4.5 8.2l2.3 2.3 4.6-4.8" fill="none" stroke="#fff" stroke-width="1.6"/></svg>Respite Care</li>
    <li><svg width="15" height="15" viewBox="0 0 16 16"><circle cx="8" cy="8" r="7" fill="none" stroke="#fff" stroke-width="1.6"/><path d="M4.5 8.2l2.3 2.3 4.6-4.8" fill="none" stroke="#fff" stroke-width="1.6"/></svg>Assisting with Daily Living Activities</li>
    <li><svg width="15" height="15" viewBox="0 0 16 16"><circle cx="8" cy="8" r="7" fill="none" stroke="#fff" stroke-width="1.6"/><path d="M4.5 8.2l2.3 2.3 4.6-4.8" fill="none" stroke="#fff" stroke-width="1.6"/></svg>Meal Preparations</li>
    <li><svg width="15" height="15" viewBox="0 0 16 16"><circle cx="8" cy="8" r="7" fill="none" stroke="#fff" stroke-width="1.6"/><path d="M4.5 8.2l2.3 2.3 4.6-4.8" fill="none" stroke="#fff" stroke-width="1.6"/></svg>Companionship</li>
    <li><svg width="15" height="15" viewBox="0 0 16 16"><circle cx="8" cy="8" r="7" fill="none" stroke="#fff" stroke-width="1.6"/><path d="M4.5 8.2l2.3 2.3 4.6-4.8" fill="none" stroke="#fff" stroke-width="1.6"/></svg>Transportation to Medical Appointments</li>
    <li><svg width="15" height="15" viewBox="0 0 16 16"><circle cx="8" cy="8" r="7" fill="none" stroke="#fff" stroke-width="1.6"/><path d="M4.5 8.2l2.3 2.3 4.6-4.8" fill="none" stroke="#fff" stroke-width="1.6"/></svg>Homemaking</li>
  </ul>
</section>

<section>
  <div class="area-map" role="img" aria-label="Map of the towns in the service area, with covered towns shaded blue"></div>
  <h2 class="form-title">CARE INQUIRY FORM</h2>
  <span class="form-label strong" style="top:2999px">Contact Information</span>
  <span class="form-label" style="top:3030px">Contact Name *</span>
  <div class="field" style="left:531px;top:3056px;width:275px">First Name</div>
  <div class="field" style="left:817px;top:3056px;width:273px">Last Name</div>
  <span class="form-label" style="top:3091px">Contact Phone Number *</span>
  <span class="form-label" style="left:820px;top:3092px">Contact Email Address *</span>
  <div class="field" style="left:531px;top:3117px;width:86px">(###)</div>
  <div class="field" style="left:625px;top:3117px;width:87px">(###)</div>
  <div class="field" style="left:720px;top:3117px;width:87px">####</div>
  <div class="field" style="left:817px;top:3117px;width:273px">Email Address *</div>
  <span class="form-label" style="top:3160px">Best Way to Reach You *</span>
  <span class="radio" style="left:537px;top:3193px"><i></i>By Phone</span>
  <span class="radio" style="left:628px;top:3193px"><i></i>By Email</span>
  <span class="form-label strong" style="top:3241px">Client Information</span>
  <span class="form-label" style="top:3272px">Client Name *</span>
  <div class="field" style="left:531px;top:3297px;width:275px">First Name</div>
  <div class="field" style="left:817px;top:3297px;width:273px">Last Name</div>
  <span class="form-label" style="top:3341px">Client Birthdate *</span>
  <div class="field" style="left:531px;top:3365px;width:86px">MM</div>
  <div class="field" style="left:625px;top:3365px;width:87px">DD</div>
  <div class="field" style="left:720px;top:3365px;width:87px">YYYY</div>
  <span class="form-label" style="top:3410px">Address Where Care Will Be Provided *</span>
  <div class="field" style="left:531px;top:3434px;width:557px">Address 1</div>
  <div class="field" style="left:531px;top:3479px;width:557px">Address 2</div>
  <div class="field" style="left:531px;top:3520px;width:275px">City</div>
  <div class="field" style="left:817px;top:3520px;width:273px">State/Province</div>
  <div class="field" style="left:531px;top:3564px;width:557px">Zip/Postal Code</div>
  <div class="field" style="left:531px;top:3608px;width:557px">Country</div>
  <span class="form-label" style="top:3651px">Please use this area to tell us more about the client and/or services that may be of interest to you. *</span>
  <div class="field" style="left:531px;top:3679px;width:557px">Message</div>
  <div class="btn-submit">Submit Care Inquiry</div>
</section>

<footer class="site-footer">
  <p class="footer-note">Thank you for considering QTR Blooms for your care needs. Information about your medical conditions, care, and financial situation that you provide to us in writing, via email, on the phone</p>
  <div class="footer-brand">QTR<br>Blooms</div>
  <div class="footer-contact" style="top:126px">
    <svg width="16" height="20" viewBox="0 0 16 20"><path d="M8 1a6 6 0 0 0-6 6c0 5 6 12 6 12s6-7 6-12a6 6 0 0 0-6-6z" fill="#fff"/><circle cx="8" cy="7" r="2.3" fill="#37a2d5"/></svg>
    <span>PO Box 418<br>Seaview, MA 02099</span>
  </div>
  <div class="footer-contact" style="top:206px">
    <svg width="18" height="18" viewBox="0 0 18 18"><path d="M4 1c1 0 3 3 3 4s-2 2-1 3 2 3 3 3 2-1 3-1 4 2 4 3-2 3-3 3C8 16 2 10 2 5c0-1 1-4 2-4z" fill="#fff"/></svg>
    <span>Tel: 555-014-2290</span>
  </div>
  <div class="footer-contact" style="top:265px">
    <svg width="20" height="16" viewBox="0 0 20 16"><rect x="1" y="2" width="18" height="12" fill="none" stroke="#fff" stroke-width="1.8"/><path d="M1 3l9 6 9-6" fill="none" stroke="#fff" stroke-width="1.8"/></svg>
    <span>Email: info@qtrblooms.com</span>
  </div>
  <p class="copyright">© 2019 Copyrights Company Name | All Rights Reserved</p>
</footer>

</body>
</html>
```